Brisbane IT support business needs our first letterhead (Contest)

Hello we are a Brisbane based Information Technology company providing support and services to small and medium sized businesses. We provide a range of services and solutions.

The business name is Harlowe Network Computing Services, or HNCS for short.

I am looking for a letterhead that looks professional (don't we all want that), but most importantly, it most utilize the colours in the logo attached, and any text used preferably in font type: HandelGotDBol.

```html
<!DOCTYPE html>
<html lang="en">
<head>
<meta charset="utf-8">
<title>Harlowe Network Computing Services – Letterhead</title>
<link rel="stylesheet" href="https://fonts.googleapis.com/css2?family=Michroma&family=Open+Sans:wght@400;600&display=swap">
<style>
  :root {
    --backdrop: #e9eaeb;
    --paper: #ffffff;
    --brand-teal: #1f4e63;
    --brand-orange: #e8792b;
    --rule-teal: #5b8397;
    --watermark-light: #f6f6f7;
    --watermark-mid: #efeff0;
    --body-text: #3d4a52;
  }
  * { margin: 0; padding: 0; box-sizing: border-box; }
  html, body {
    width: 1200px;
    height: 1192px;
    overflow: hidden;
    background: var(--backdrop);
  }
  .letterhead {
    position: absolute;
    left: 211px;
    top: 46px;
    width: 778px;
    height: 1100px;
    background: var(--paper);
    box-shadow: 0 2px 10px rgba(0,0,0,0.08);
  }
  .rule {
    position: absolute;
    left: 70px;
    right: 70px;
    height: 1.5px;
    background: var(--rule-teal);
  }
  .rule--head-top { top: 92px; }
  .rule--head-bottom { top: 210px; }
  .rule--foot-top { top: 858px; }
  .rule--foot-bottom { top: 1012px; }

  .brand {
    position: absolute;
    top: 122px;
    left: 0;
    right: 0;
    display: flex;
    justify-content: center;
    align-items: center;
    gap: 14px;
  }
  .brand__dot {
    width: 56px;
    height: 56px;
    border-radius: 50%;
    background: var(--brand-teal);
  }
  .brand__name {
    font-family: "Michroma", sans-serif;
    font-size: 26px;
    color: var(--brand-orange);
    letter-spacing: 1px;
  }

  .watermark {
    position: absolute;
    left: 50%;
    top: 262px;
    width: 420px;
    height: 420px;
    margin-left: -210px;
    border-radius: 50%;
    background: radial-gradient(circle at 50% 40%, var(--watermark-light) 0%, var(--watermark-mid) 100%);
  }

  .footer {
    position: absolute;
    top: 880px;
    left: 0;
    right: 0;
    text-align: center;
  }
  .footer__company {
    font-family: "Michroma", sans-serif;
    font-size: 16px;
    color: var(--brand-teal);
    letter-spacing: 0.5px;
    text-transform: uppercase;
    -webkit-text-stroke: 0.4px var(--brand-teal);
  }
  .footer__contact {
    margin-top: 16px;
    font-family: "Open Sans", sans-serif;
    font-size: 12px;
    line-height: 22px;
    color: var(--body-text);
  }
  .footer__label { color: var(--brand-orange); font-weight: 600; }
  .footer__sep { color: var(--brand-orange); margin: 0 6px; }
</style>
</head>
<body>
  <main class="letterhead">
    <div class="rule rule--head-top"></div>
    <header class="brand">
      <span class="brand__dot"></span>
      <span class="brand__name">HNCS</span>
    </header>
    <div class="rule rule--head-bottom"></div>

    <div class="watermark" role="img" aria-label="Faint brand emblem watermark"></div>

    <div class="rule rule--foot-top"></div>
    <footer class="footer">
      <p class="footer__company">Harlowe Network Computing Services</p>
      <p class="footer__contact">
        <span class="footer__label">a:</span> Your Commercial or office address<span class="footer__sep">|</span><span class="footer__label">p:</span> 00.00.00.0000<span class="footer__sep">|</span><span class="footer__label">f:</span> 00.00.00.0000<br>
        <span class="footer__label">e:</span> yourname@yourwebsite.com<span class="footer__sep">|</span><span class="footer__label">w:</span> www.yourwebsite.com
      </p>
    </footer>
    <div class="rule rule--foot-bottom"></div>
  </main>
</body>
</html>
```